Website To Serve As A Resource For Medical Conditions

I need a website that is attractive that will be utilized to educate patients on either hepatitis c or HIV so it should be easily readable attractive but also professional. This website is going to be furnished with various topics for example, HIV treatment, HIV and Nutrition, HIV and Exercise, HIV and....

This website will also be cloned and utilized similarly for Hepatitis.

Coded - Design and coding required

1 page

0094D4
00A9DD
6FCCEA
C7EBF8
E9F6FB
A7469A
B969AE
D3A5CF
EDDBEB
F8F0F9
6B429C
8869AF
B7A5CE
E3DAEB
F3F0F8

```html
<!DOCTYPE html>
<html lang="en">
<head>
<meta charset="utf-8">
<title>HIV Information Resource</title>
<link href="https://fonts.googleapis.com/css2?family=Poppins:wght@400;500;600;700&display=swap" rel="stylesheet">
<style>
:root{
  --blue-deep:#0094D4;
  --blue:#00A9DD;
  --blue-light:#6FCCEA;
  --blue-pale:#C7EBF8;
  --blue-mist:#E9F6FB;
  --magenta:#A7469A;
  --magenta-soft:#B969AE;
  --purple:#6B429C;
  --purple-mid:#8869AF;
  --purple-pale:#F8F0F9;
  --violet-bar:#7B4EA0;
  --section-grey:#EEF3F6;
  --text:#4a4a4a;
  --text-soft:#6b6b6b;
  --rule:#b9b9b9;
}
*{box-sizing:border-box;margin:0;padding:0}
html,body{width:1200px;height:3725px;overflow:hidden}
body{position:relative;font-family:'Poppins',sans-serif;color:var(--text);background:#fff}
.abs{position:absolute}

/* header */
.site-header{position:absolute;left:0;top:0;width:1200px;height:115px;background:#fff}
.brand{left:127px;top:30px;display:flex;align-items:center;gap:12px;font-size:24px;font-weight:600;color:var(--purple)}
.brand-dot{width:40px;height:40px;border-radius:50%;background:var(--magenta-soft)}
.main-nav a{position:absolute;top:50px;font-size:16px;color:#555;text-decoration:none}
.main-nav .active{color:#333;font-weight:500}
.main-nav .active::after{content:"";position:absolute;left:-5px;right:-5px;top:34px;height:5px;border-radius:3px;background:var(--purple-mid)}
.search{left:811px;top:35px;width:262px;height:49px;border:1.5px solid var(--magenta-soft);border-radius:10px;font-size:14px;color:#aaa;padding:13px 20px}
.search svg{position:absolute;right:12px;top:14px}

/* hero */
.hero{left:0;top:115px;width:1200px;height:526px;background:radial-gradient(circle at 28% 38%,#b0305f 0,#c14a88 18%,transparent 32%),radial-gradient(circle at 50% 72%,#b04080 0,transparent 16%),linear-gradient(100deg,#b79be0 0%,#cfa8e6 45%,#b07fd0 80%,#8a55b0 100%)}
.hero h1{position:absolute;left:620px;width:452px;top:306px;text-align:center;color:#fff;font-size:31px;font-weight:700;line-height:37px;text-transform:uppercase}

/* section headings */
.section-title{font-size:32px;font-weight:600;color:#666}
.rule{height:2px;background:#aaa}
.rule-accent{height:7px;width:70px;border-radius:2px;background:linear-gradient(90deg,var(--blue-deep),var(--blue-light))}

.info-band{left:0;top:641px;width:1200px;height:459px;background:var(--section-grey)}
.view-more{left:978px;top:706px;font-size:17px;font-weight:500;color:#666}
.topic-card{position:absolute;top:784px;width:217px}
.topic-card .photo{height:143px}
.topic-card h3{margin-top:20px;font-size:21px;font-weight:500;color:#333}
.topic-card p{margin-top:13px;font-size:17px;line-height:22px;color:#666}

/* more info */
.subtitle{font-size:21px;color:#555}
.fact{position:absolute;left:642px;width:415px;font-size:18px;line-height:22px;color:#555}
.fact-rule{position:absolute;left:642px;width:412px;height:2px;background:#ccc}

/* news */
.news-item{position:absolute;width:460px;height:110px}
.news-item .photo{position:absolute;left:0;top:0;width:179px;height:110px}
.news-item h3{position:absolute;left:200px;top:4px;font-size:21px;font-weight:400;color:#333}
.news-item p{position:absolute;left:200px;top:38px;width:240px;font-family:Arial,sans-serif;font-size:14px;line-height:18px;color:#888}

/* research */
.research{left:0;top:2412px;width:1200px;height:593px;background:linear-gradient(120deg,#0f8fcf 0%,#1ea8e0 55%,#40c6f0 100%)}
.research .section-title{color:#fff;font-weight:700}
.research-links a{position:absolute;left:127px;width:258px;font-size:17px;font-weight:500;color:#fff;text-decoration:none;padding-bottom:10px;border-bottom:1.5px solid rgba(255,255,255,.45)}
.research-links a:last-child{border-bottom:none}
.note{position:absolute;left:599px;width:474px;height:106px;background:rgba(255,255,255,.18);border-left:14px solid rgba(255,255,255,.25);padding:20px 28px;color:#fff;font-size:18px;line-height:22px;font-weight:500}

/* newsletter */
.signup-title{left:0;width:1200px;top:3083px;text-align:center;font-size:28px;font-weight:600;line-height:31px;color:#666}
.email{left:253px;top:3170px;width:545px;height:59px;border:1.5px solid #999;padding:18px 12px;font-size:16px;color:#555}
.signup-btn{left:805px;top:3170px;width:141px;height:59px;background:linear-gradient(90deg,var(--purple),var(--magenta-soft));color:#fff;font-size:15px;font-weight:600;text-align:center;line-height:59px}

/* footer */
.site-footer{left:0;top:3296px;width:1200px;height:347px;background:var(--purple-pale)}
.footer-title{position:absolute;font-size:24px;color:#222}
.footer-col{position:absolute;top:3437px;list-style:none;font-size:16px;line-height:29px;color:#777}
.footer-divider{position:absolute;top:3401px;width:2px;height:185px;background:var(--blue-deep)}
.bottom-bar{left:0;top:3643px;width:1200px;height:82px;background:var(--violet-bar);color:#fff;font-size:15px}
.bottom-bar p{position:absolute;left:127px;top:30px}
.social{position:absolute;top:33px;width:16px;height:16px;border-radius:50%;background:#fff}
</style>
</head>
<body>

<header class="site-header">
  <div class="brand abs"><span class="brand-dot"></span>Logo Name</div>
  <nav class="main-nav">
    <a class="active" href="#" style="left:362px">Home</a>
    <a href="#" style="left:463px">About Us</a>
    <a href="#" style="left:587px">About HIV</a>
    <a href="#" style="left:720px">News</a>
  </nav>
  <div class="search abs">Enter Keyword
    <svg width="20" height="20" viewBox="0 0 20 20"><circle cx="8" cy="8" r="6" fill="none" stroke="#8869AF" stroke-width="2.5"/><line x1="12.5" y1="12.5" x2="18" y2="18" stroke="#8869AF" stroke-width="2.8" stroke-linecap="round"/></svg>
  </div>
</header>

<section class="hero abs" role="img" aria-label="Close-up illustration of virus particles in magenta and purple tones">
  <h1>What HIV information are you looking for?</h1>
</section>

<section class="info-band abs">
  <h2 class="section-title abs" style="left:125px;top:58px">HIV Information</h2>
</section>
<span class="view-more abs">View More</span>
<div class="rule abs" style="left:127px;top:755px;width:943px"></div>
<div class="rule-accent abs" style="left:127px;top:751px"></div>

<article class="topic-card" style="left:127px"><div class="photo" role="img" aria-label="Hand holding medication pills" style="background:linear-gradient(135deg,#d8d8da,#b9bcc2)"></div><h3>HIV treatment</h3><p>Lorem ipsum dolor sit ame consectetur adipiscing</p></article>
<article class="topic-card" style="left:369px"><div class="photo" role="img" aria-label="Box of fresh vegetables" style="background:linear-gradient(135deg,#6f7a55,#b5884f)"></div><h3>HIV and Nutrition</h3><p>Lorem ipsum dolor sit ame consectetur adipiscing</p></article>
<article class="topic-card" style="left:612px"><div class="photo" role="img" aria-label="Runner on a road at sunset" style="background:linear-gradient(180deg,#7a5a45,#3a302c)"></div><h3>HIV and Exercise</h3><p>Lorem ipsum dolor sit ame consectetur adipiscing</p></article>
<article class="topic-card" style="left:855px"><div class="photo" role="img" aria-label="Gloved hand holding a blood sample tube" style="background:linear-gradient(135deg,#2aa7d8,#c2324a 70%)"></div><h3>HIV and Hepatitis</h3><p>Lorem ipsum dolor sit ame consectetur adipiscing</p></article>

<h2 class="section-title abs" style="left:125px;top:1160px">More Information About HIV</h2>
<p class="subtitle abs" style="left:125px;top:1203px">Clear and reliable information on all aspects of HIV.</p>
<div class="rule abs" style="left:127px;top:1257px;width:943px"></div>
<div class="rule-accent abs" style="left:127px;top:1253px"></div>

<div class="abs" role="img" aria-label="Gloved hand holding a labelled blood test tube in a laboratory" style="left:127px;top:1294px;width:477px;height:441px;background:linear-gradient(135deg,#c9d6c8 0%,#e8eef2 45%,#b83040 55%,#dfe6ee 70%)"></div>
<p class="fact" style="top:1311px">Lorem ipsum dolor sit amet, consectetur adip iscing elit, sed do eiusmod tempor incididunt ut labore et dolore magna aliqua.</p>
<div class="fact-rule" style="top:1400px"></div>
<p class="fact" style="top:1426px">Lorem ipsum dolor sit amet, consectetur adip iscing elit, sed do eiusmod tempor incididunt ut labore et dolore magna aliqua.</p>
<div class="fact-rule" style="top:1518px"></div>
<p class="fact" style="top:1540px">Lorem ipsum dolor sit amet, consectetur adip iscing elit, sed do eiusmod tempor incididunt ut labore et dolore magna aliqua.</p>
<div class="fact-rule" style="top:1633px"></div>
<p class="fact" style="top:1655px">Lorem ipsum dolor sit amet, consectetur adip iscing elit, sed do eiusmod tempor incididunt ut labore et dolore magna aliqua.</p>

<div class="abs" style="left:127px;top:1801px;width:946px;height:2px;background:#ddd"></div>

<h2 class="section-title abs" style="left:125px;top:1850px">More News about HIV</h2>

<article class="news-item" style="left:127px;top:1929px"><div class="photo" role="img" aria-label="Microscopic view of virus cells" style="background:linear-gradient(135deg,#7d8b93,#a93a4a)"></div><h3>HIV Overview</h3><p>Lorem ipsum dolor sit ame consec tetur adipiscing loelised do eiusm od tempomaecenas.</p></article>
<article class="news-item" style="left:639px;top:1929px"><div class="photo" role="img" aria-label="Single virus particle on orange background" style="background:radial-gradient(circle,#b22a2a 0,#e0661d 45%,#f2b21e 100%)"></div><h3>Living with HIV</h3><p>Lorem ipsum dolor sit ame consec tetur adipiscing loelised do eiusm od tempomaecenas.</p></article>
<article class="news-item" style="left:127px;top:2065px"><div class="photo" role="img" aria-label="Pregnant belly" style="background:linear-gradient(90deg,#9db0b8,#e7e2dd 55%,#8fc8dc)"></div><h3>HIV and Pregnancy</h3><p>Lorem ipsum dolor sit ame consec tetur adipiscing loelised do eiusm od tempomaecenas.</p></article>
<article class="news-item" style="left:639px;top:2065px"><div class="photo" role="img" aria-label="Skin rash on the torso" style="background:linear-gradient(90deg,#6f8a8a,#c99a86 50%,#6a7f95)"></div><h3>HIV/aids symptoms</h3><p>Lorem ipsum dolor sit ame consec tetur adipiscing loelised do eiusm od tempomaecenas.</p></article>
<article class="news-item" style="left:127px;top:2201px"><div class="photo" role="img" aria-label="Couple talking together on a sofa" style="background:linear-gradient(90deg,#8c7a6a,#b49a82 50%,#6d6258)"></div><h3>Living with HIV</h3><p>Lorem ipsum dolor sit ame consec tetur adipiscing loelised do eiusm od tempomaecenas.</p></article>
<article class="news-item" style="left:639px;top:2201px"><div class="photo" role="img" aria-label="Patient consulting with a doctor" style="background:linear-gradient(90deg,#3a3f55,#c8ccd4 60%,#e4e6ea)"></div><h3>Sexual health</h3><p>Lorem ipsum dolor sit ame consec tetur adipiscing loelised do eiusm od tempomaecenas.</p></article>

<section class="research abs">
  <h2 class="section-title abs" style="left:125px;top:50px">Research &amp; Science</h2>
  <div class="abs" style="left:127px;top:110px;width:943px;height:2px;background:rgba(255,255,255,.75)"></div>
  <div class="abs" style="left:127px;top:106px;width:70px;height:7px;background:linear-gradient(90deg,#6B429C,#B969AE)"></div>
</section>
<nav class="research-links">
  <a href="#" style="top:2553px">Donec gravida feod</a>
  <a href="#" style="top:2599px">Aliquam facilisis nullaibus.</a>
  <a href="#" style="top:2645px">Nulla fermentum est eravida.</a>
  <a href="#" style="top:2692px">Vestibulum at sales rhoncus.</a>
  <a href="#" style="top:2738px">Nullam quis fut semper.</a>
  <a href="#" style="top:2785px">Ut a nisi eu odtum hendrerit.</a>
  <a href="#" style="top:2831px">Qulum quis sed arcu.</a>
  <a href="#" style="top:2877px">Donec laci maximus.</a>
</nav>
<div class="note" style="top:2558px">Lorem ipsum dolor sit amet, consectetur adip iscing elit, sed do eiusmod tempor incididunt ut labore et dolore magna aliqua.</div>
<div class="note" style="top:2679px">Lorem ipsum dolor sit amet, consectetur adip iscing elit, sed do eiusmod tempor incididunt ut labore et dolore magna aliqua.</div>
<div class="note" style="top:2800px">Lorem ipsum dolor sit amet, consectetur adip iscing elit, sed do eiusmod tempor incididunt ut labore et dolore magna aliqua.</div>

<h2 class="signup-title abs">Lorem ipsum dolor sit amet, consectetur<br>adipiscing elit, sed do eiusmod</h2>
<div class="email abs">Email:</div>
<div class="signup-btn abs">SIGN UP</div>

<footer class="site-footer abs"></footer>
<h3 class="footer-title" style="left:127px;top:3380px;font-weight:700">More Links</h3>
<h3 class="footer-title" style="left:943px;top:3388px;font-weight:400">About</h3>
<ul class="footer-col" style="left:127px"><li>HIV Overview</li><li>HIV Prevention</li><li>HIV Treatment</li><li>Side Effects of HIV Medicines</li><li>HIV and Pregnancy</li></ul>
<div class="footer-divider" style="left:363px"></div>
<ul class="footer-col" style="left:405px"><li>Recently diagnosed with HIV</li><li>Testing &amp; health monitoring</li><li>HIV treatment</li><li>Symptoms of HIV</li></ul>
<div class="footer-divider" style="left:650px"></div>
<ul class="footer-col" style="left:709px"><li>Hepatitis &amp; HIV</li><li>HIV and Nutrition</li><li>HIV and Exercise</li><li>Living with HIV</li></ul>
<div class="footer-divider" style="left:881px"></div>
<ul class="footer-col" style="left:943px"><li>Home</li><li>About Us</li><li>About HIV</li><li>News</li><li>Privacy Policy</li></ul>

<div class="bottom-bar abs">
  <p>Copyright 2023 All rights are reserved.</p>
  <span class="social" style="left:990px"></span>
  <span class="social" style="left:1022px"></span>
  <span class="social" style="left:1053px"></span>
</div>

</body>
</html>
```